UK Supplement Company Needs a Label for Diet Protein Powder

We need a new, modern and fresh design for our Diet Protein Powder. Our protein powder is packaged in black plastic tubs (photo attached) and needs an attractive label. We would like to see designs that grab attention and look professional. We're very open to ideas. The label should be 88mm x 365mm. We also prefer PSD format where possible. These alterations could be made once your design is chosen. Have attached photo of our shake ingredients/benefits.
Updates

Need extra days to review

Target Market(s)

Slimmers

Industry/Entity Type

Health And Wellness

Font styles to use
Serif
Sans Serif

Colors

Designer to choose colors to be used in the design.

Requirements
Must have
• Clean, Modern and Professional Look. Eye catching. The flavour, we offer 6 flavours so this must be something we can edit (Flavours are Banana, Chocolate, Chocolate Mint, Strawberry, Toffee and Vanilla).
Nice to have
• Our logo, this can be VELTRO Nutrition or just VELTRO. Our logo files are attached.
Should not have
• We do not want to see people (faces or bodies) on the design.

```html
<!DOCTYPE html>
<html lang="en">
<head>
<meta charset="utf-8">
<title>VELTRO Nutrition – Protein Powder Label</title>
<link href="https://fonts.googleapis.com/css2?family=Open+Sans:wght@400;600;700;800&display=swap" rel="stylesheet">
<style>
  :root {
    --backdrop: #e9e9e9;
    --label-black: #0d0d0d;
    --panel-dark: #1b1b1b;
    --ink-white: #e6e6e6;
    --accent-green: #8cc63f;
    --accent-peach: #e6c2aa;
    --band-text: #1a1a1a;
  }
  * { margin: 0; padding: 0; box-sizing: border-box; }
  html, body {
    width: 1200px; height: 960px; overflow: hidden;
    background: var(--backdrop);
    font-family: "Open Sans", Arial, sans-serif;
  }
  .label {
    position: absolute; left: 40px; top: 235px;
    width: 1120px; height: 490px;
    background: var(--label-black);
  }
  .side-tag { position: absolute; background: var(--accent-green); }
  .side-tag--left { left: 0; top: 195px; width: 14px; height: 30px; }
  .side-tag--right {
    right: 0; top: 200px; width: 70px; height: 60px;
    padding: 6px 8px; font-size: 8px; font-weight: 700; color: var(--band-text);
  }
  .ingredients-box {
    position: absolute; left: 0; top: 310px; width: 26px; height: 90px;
    background: var(--panel-dark);
  }
  .brand {
    position: absolute; left: 0; right: 0; top: 92px;
    display: flex; justify-content: center; align-items: center; gap: 10px;
  }
  .brand-dot { width: 12px; height: 12px; border-radius: 50%; background: var(--accent-green); }
  .brand-name {
    font-size: 40px; font-weight: 700; color: var(--ink-white); letter-spacing: -0.5px;
    white-space: nowrap;
  }
  .product { position: absolute; left: 462px; top: 232px; line-height: 1; }
  .product-kicker { font-size: 15px; font-weight: 700; color: var(--accent-green); }
  .product-name {
    font-size: 54px; font-weight: 800; color: var(--ink-white);
    line-height: 0.88; margin-top: 5px; letter-spacing: -0.5px;
  }
  .product-claim { font-size: 17px; font-weight: 600; color: var(--ink-white); margin-top: 6px; }
  .product-flavour { font-size: 18px; font-weight: 700; color: var(--accent-peach); margin-top: 3px; }
  .product-stats { font-size: 8.5px; font-weight: 700; color: var(--accent-green); margin-top: 5px; white-space: nowrap; }
  .weight-band {
    position: absolute; left: 0; right: 0; bottom: 22px; height: 13px;
    background: var(--accent-peach);
    font-size: 7px; font-weight: 700; color: var(--band-text);
    padding-left: 526px; line-height: 13px; white-space: nowrap;
  }
</style>
</head>
<body>
  <main class="label">
    <div class="side-tag side-tag--left"></div>
    <div class="side-tag side-tag--right">Nutrition Facts</div>
    <div class="ingredients-box"></div>

    <header class="brand">
      <span class="brand-name">VELTRO Nutrition</span>
      <span class="brand-dot"></span>
    </header>

    <section class="product">
      <p class="product-kicker">DIETARY SUPPLEMENT</p>
      <h1 class="product-name">PROTEIN<br>POWDER</h1>
      <p class="product-claim">LOW CALORIE</p>
      <p class="product-flavour">FLAVOUR&nbsp; VANILLA</p>
      <p class="product-stats">21G PROTEIN • 117 CALORIES • 4.2 CARBS PER SERVING</p>
    </section>

    <div class="weight-band">NET WT 29.3 OZ (1.83 LB) 832 G</div>
  </main>
</body>
</html>
```